Invitation Design Project

I would like to have a custom invitation (and reception/response cards) designed for my son's Bar Mitzvah. I have a strong idea of what I want and have a few mock-ups, but my "home made" effort would be improved by the addition of professional creativity and skill. The invitation should be white, red, and black, and a bold typographic style (see attachment). I am looking for a clean modern feel, and prefer square shaped invitations. I need the final product in an electronic format that I could either print myself or have done at a local printer.

Target Market(s)

Guests to a Bar Mitzvah. A group of family and friends ranging from 40-60 years of age, and a group of my son's 13 year old friends.

Industry/Entity Type

Electronic

Requirements
Must have
• Square shaped invitation (exact dimensions in attached file)
Typographic style
Red, black, white
Red color should be CMYK: 30-96-76-26
Nice to have
• I like the two icons on my attached sample reception card, especially the swirl/Torah one. I would be nice to use these (or similar ones) if there is a way to do so, but this is not a requirement.

```html
<!DOCTYPE html>
<html lang="en">
<head>
<meta charset="utf-8">
<title>Nolan's Bar Mitzvah Invitation</title>
<link rel="stylesheet" href="https://fonts.googleapis.com/css2?family=Didact+Gothic&family=Noto+Sans:wght@400;500&family=Oswald:wght@400&display=swap">
<style>
  :root {
    --maroon: #8e1f2e;
    --maroon-deep: #3a0d13;
    --maroon-soft: #b0747a;
    --grey-band: #d9d5d5;
    --black: #000000;
    --white: #ffffff;
    --ink: #111111;
    --backdrop: #ecebeb;
  }
  html, body {
    margin: 0;
    padding: 0;
    width: 1200px;
    height: 836px;
    overflow: hidden;
    background: var(--backdrop);
  }
  .invitation {
    position: absolute;
    left: 182px;
    top: 0;
    width: 836px;
    height: 836px;
    overflow: hidden;
    background: var(--white);
    font-family: "Noto Sans", sans-serif;
  }
  .block {
    position: absolute;
    box-sizing: border-box;
    display: flex;
    align-items: center;
    white-space: nowrap;
    margin: 0;
  }
  .top-band {
    left: 0; top: 0; width: 836px; height: 50px;
    background: linear-gradient(90deg, var(--maroon-deep) 0%, #6b1c26 45%, var(--maroon-deep) 100%);
  }
  .opening-line {
    left: 0; top: 50px; width: 836px; height: 65px;
    justify-content: center;
    background: var(--white);
    font-family: "Didact Gothic", sans-serif;
    font-size: 31px;
    color: var(--ink);
  }
  .invite-line {
    left: 0; top: 115px; width: 836px; height: 65px;
    justify-content: center;
    background: var(--grey-band);
    font-family: "Didact Gothic", sans-serif;
    font-size: 30px;
    color: var(--maroon);
  }
  .name-side {
    left: 0; top: 180px; width: 290px; height: 310px;
    background: var(--black);
  }
  .name-panel {
    position: absolute;
    left: 290px; top: 180px; width: 546px; height: 310px;
  }
  .name-panel svg { display: block; }
  .celebrate-lead {
    left: 0; top: 490px; width: 372px; height: 58px;
    background: var(--maroon-soft);
  }
  .celebrate-line {
    left: 372px; top: 490px; width: 464px; height: 58px;
    justify-content: center;
    background: var(--white);
    border: 2px solid var(--black);
    font-size: 27px;
    color: var(--ink);
  }
  .accent { color: var(--maroon); }
  .date-line {
    left: 0; top: 548px; width: 716px; height: 56px;
    padding-left: 10px;
    background: var(--maroon);
    color: var(--white);
    font-size: 19px;
    font-weight: 500;
  }
  .date-line small { font-size: 14px; }
  .date-tail {
    left: 716px; top: 548px; width: 120px; height: 56px;
    background: var(--black);
  }
  .time-line {
    left: 390px; top: 612px; width: 410px; height: 56px;
    justify-content: center;
    background: var(--maroon);
    color: var(--white);
    font-size: 25px;
  }
  .venue-line {
    left: 0; top: 672px; width: 620px; height: 54px;
    padding-left: 10px;
    background: var(--black);
    color: var(--white);
    font-size: 26px;
  }
  .address-line {
    left: 0; top: 726px; width: 620px; height: 54px;
    padding-left: 10px;
    background: var(--white);
    color: var(--maroon);
    font-size: 26px;
  }
  .address-tail {
    left: 620px; top: 726px; width: 216px; height: 54px;
    background: var(--black);
  }
  .hosts {
    left: 0; top: 780px; width: 150px; height: 56px;
    padding-right: 10px;
    justify-content: flex-end;
    text-align: right;
    background: var(--black);
    color: var(--white);
    font-size: 20px;
    line-height: 1.15;
  }
  .kiddush-line {
    left: 150px; top: 780px; width: 686px; height: 56px;
    padding-left: 12px;
    background: var(--maroon);
    color: var(--white);
    font-size: 18px;
    font-weight: 500;
  }
</style>
</head>
<body>
  <main class="invitation">
    <div class="block top-band"></div>
    <p class="block opening-line">It is with great PRIDE and JOY that</p>
    <p class="block invite-line">WE INVITE YOU to join us as OUR SON</p>

    <div class="block name-side"></div>
    <div class="name-panel">
      <svg width="546" height="310" viewBox="0 0 546 310" xmlns="http://www.w3.org/2000/svg">
        <defs>
          <linearGradient id="nameFill" x1="0" y1="0" x2="0" y2="1">
            <stop offset="0" stop-color="#3a0d13"/>
            <stop offset="0.55" stop-color="#7a1c28"/>
            <stop offset="1" stop-color="#8e1f2e"/>
          </linearGradient>
        </defs>
        <rect width="546" height="310" fill="url(#nameFill)"/>
        <text x="4" y="296" textLength="536" lengthAdjust="spacingAndGlyphs"
              font-family="'Oswald', sans-serif" font-size="372" fill="#ffffff">NOLAN</text>
      </svg>
    </div>

    <div class="block celebrate-lead"></div>
    <p class="block celebrate-line">CELEBRATES HIS&nbsp;<span class="accent">BAR MITZVAH</span></p>

    <p class="block date-line">Saturday, September TWENTY eighth, two thousand&nbsp;<small>and</small>&nbsp;THIRTEEN</p>
    <div class="block date-tail"></div>

    <p class="block time-line">Ten THIRTY in the Morning</p>

    <p class="block venue-line">Eastbrook Valley Hebrew Congregation</p>
    <p class="block address-line">2250 Maple Grove Avenue Linden, Virginia</p>
    <div class="block address-tail"></div>

    <p class="block hosts">Rachel<br>Stein</p>
    <p class="block kiddush-line">Please join us for a KIDDUSH immediately following the service</p>
  </main>
</body>
</html>
```